Financial Markets Algorithmic Trading solution needs One pager Marketing designs

We are creating Marketing sheets that will be handed to potential clients that will give a broad base of our products available. We are an established Sell side firm in the financial Industry and our product focus is a Technology base solution and we want to showcases our Algorithmic trading suite.
Our customer base is Buy-side Traders,hedge funds, managing directors. We want a clean high end technology based look that will encompass the colors that are in our logo.
We intend to work with the designer after initial design to encompass the theme to other pages we have. So we will need a design that can be part of a set but can stand alone.

** i have uploaded a new File that is the correct File to design to. Please follow the flow of the categories and what resides under those headers. This is key for the delivery of the material****

Target Market(s)

Finance- Buy side firms, geared for meetings and info sheets to be left with clients who are CEO's , Head Traders, Managing Directors

Industry/Entity Type

Financial Service

Font styles to use
Other font styles liked:
• Tw Cen MT

Requirements
Must have
• Must include the logo, and encompass the colors that are in the logo.
• We want this to have a Technology company feel to it. We would like it clean and unique, all while not falling into the normal classic business look.
• Also for this page we would like to keep the layout similar to what we have.
• Please keep the style of lettering
Should not have
• Messy look, overpowering color. no cartoon graphics

```html
<!DOCTYPE html>
<html lang="en">
<head>
<meta charset="utf-8">
<title>Algorithmic Trading Strategy Overview</title>
<link href="https://fonts.googleapis.com/css2?family=Jost:wght@400;500;700&display=swap" rel="stylesheet">
<style>
  :root{
    --stage:#d9d9db;
    --slate:#9ea7c4;
    --sky:#bfe3f3;
    --orange:#f7941d;
    --blue:#0a7cc1;
    --ink:#1f2a44;
    --body:#3a4258;
    --rule:#8a93a8;
    --paper:#f4f7fb;
  }
  *{box-sizing:border-box;margin:0;padding:0}
  html,body{width:1200px;height:960px;overflow:hidden}
  body{background:var(--stage);font-family:"Jost",sans-serif;position:relative}
  .sheet{position:absolute;left:260px;top:40px;width:680px;height:880px;background:var(--paper);overflow:hidden;box-shadow:0 10px 30px rgba(0,0,0,.25)}
  .hero-bg{position:absolute;left:0;top:0;width:680px;height:450px;background:linear-gradient(100deg,var(--slate) 0%,#b8c3dc 40%,var(--sky) 75%,#d7eff9 100%)}
  .circuit-bg{position:absolute;left:0;top:450px;width:680px;height:430px;background:linear-gradient(180deg,#ffffff 0%,#eef3f8 60%,#e3ebf3 100%)}
  .shapes{position:absolute;left:0;top:0}
  .portrait{position:absolute;left:420px;top:430px;width:260px;height:450px;background:linear-gradient(160deg,#6a5aa8 0%,#8d6fb5 40%,#c89a7e 75%,#d9a9b8 100%);clip-path:polygon(30% 0,100% 0,100% 100%,0 100%,0 55%)}
  .logo-band{position:absolute;left:390px;top:150px;width:290px;height:80px;background:#fff;clip-path:polygon(10% 0,100% 0,100% 100%,10% 100%,0 50%);display:flex;align-items:center;padding-left:42px;gap:10px}
  .logo-dot{width:28px;height:28px;border-radius:50%;background:var(--orange);flex:none}
  .logo-name{font-size:20px;font-weight:500;color:var(--blue);white-space:nowrap}
  .title{position:absolute;left:62px;top:36px;font-size:20px;font-weight:500;color:#fff;letter-spacing:.3px}
  .title-mark{position:absolute;left:22px;top:32px}
  .intro{position:absolute;left:24px;top:74px;width:350px;font-size:11px;line-height:15px;font-weight:700;color:var(--ink);text-align:justify}
  .intro b{font-size:12.5px}
  .strategies{position:absolute;left:20px;top:460px;width:385px;display:flex;flex-direction:column;gap:6px}
  .group{display:flex;gap:8px}
  .group-label{writing-mode:vertical-rl;font-size:12px;font-weight:700;text-align:center;white-space:nowrap;flex:none}
  .label-orange{color:var(--orange)}
  .label-blue{color:var(--blue)}
  .group-items{flex:1;border-left:1px solid var(--rule);padding-left:9px}
  .strategy{padding:5px 0 6px;border-bottom:1px solid var(--rule)}
  .strategy:last-child{border-bottom:none}
  .strategy h3{font-size:10px;font-weight:700;color:var(--ink);letter-spacing:.3px}
  .strategy p{font-size:9px;line-height:11.5px;color:var(--body)}
</style>
</head>
<body>
<main class="sheet">
  <div class="hero-bg" role="img" aria-label="Soft blue background with faint interlocking gears"></div>
  <div class="circuit-bg" role="img" aria-label="Pale background with faint circuit board lines"></div>

  <svg class="shapes" width="680" height="880" viewBox="0 0 680 880" aria-hidden="true">
    <polygon points="560,230 680,230 680,600 520,560" fill="#a9dcf2"/>
    <polygon points="328,290 268,416 452,426" fill="#fff"/>
    <polygon points="330,300 280,410 440,420" fill="var(--blue)"/>
    <polygon points="350,318 660,380 520,640" fill="var(--orange)"/>
  </svg>

  <div class="portrait" role="img" aria-label="Photograph of a person overlaid with circuit board patterns, holding a pen"></div>

  <div class="logo-band">
    <span class="logo-dot"></span>
    <span class="logo-name">Marlowe &amp; Partners</span>
  </div>

  <svg class="title-mark" width="40" height="40" viewBox="0 0 40 40" aria-hidden="true">
    <polygon points="2,2 36,2 2,26" fill="#fff"/>
    <polygon points="2,18 28,38 2,38" fill="var(--orange)"/>
  </svg>
  <h1 class="title">Algorithmic Trading Strategy Overview</h1>

  <p class="intro"><b>Marlowe &amp; Partners</b> has partnered with an award winning algorithmic trading platform and developed a custom suite of algorithms designed to ensure high quality execution. Our algorithms incorporate our unique Harborline point of sale order types (xQuote™ / zQuote™) seamlessly into each strategy. This integration smooths workflow, improves execution quality, ensures greater liquidity sourcing, minimizes information leakage and brings a wide variety of Algo and SOR strategies directly into your OMS, EMS, or proprietary trading platform. In addition, we work in a consultative role to develop custom DMA routes, design algorithms according to client needs or specific requirements, &amp; implement unique routing strategies designed to efficiently touch today's complex market micro-strategy.</p>

  <div class="strategies">
    <section class="group">
      <h2 class="group-label label-orange">Liquidity Sourcing</h2>
      <div class="group-items">
        <article class="strategy">
          <h3>"SOR"</h3>
          <p>Optimizes order placement in lit and dark venues to maximize liquidity capture and minimize information leakage. The strategy balances Urgency to capture the display quote vs. opportunities to seek out dark liquidity to minimize information leakage and price improvement.</p>
        </article>
        <article class="strategy">
          <h3>DARK AGG</h3>
          <p>Manages order placement in dark venues to optimize liquidity capture and reduce information leakage. The strategy attempts to first discover liquidity by slicing optimally sized orders at various venues, and then rebalances intelligently to venues where it has detected liquidity.</p>
        </article>
      </div>
    </section>

    <section class="group">
      <h2 class="group-label label-blue">Schedule Driven</h2>
      <div class="group-items">
        <article class="strategy">
          <h3>"VWAP"</h3>
          <p>Trades using historical volume profile to target VWAP as the benchmark. The strategy can optionally accept StartTime and EndTime as parameters to schedule trading in a given trading period. The strategy utilizes passive and aggressive trading tactics to achieve liquidity.</p>
        </article>
        <article class="strategy">
          <h3>"TWAP"</h3>
          <p>Similar to the VWAP strategy with a different schedule. The schedule is a constant rate of trading between the given StartTime and EndTime.</p>
        </article>
      </div>
    </section>

    <section class="group">
      <h2 class="group-label label-orange">Dynamic &amp; Adaptive</h2>
      <div class="group-items">
        <article class="strategy">
          <h3>"POV"</h3>
          <p>Tracks volume from the time the order starts trading and trades according to the specified target participation percentage. Continuous optimizations are made as the order trades to target optimal price and liquidity goals.</p>
        </article>
        <article class="strategy">
          <h3>"ARRIVAL PRICE"</h3>
          <p>Manages the trade-off between market impact and volatility (price risk) to optimally execute the order.</p>
        </article>
      </div>
    </section>
  </div>
</main>
</body>
</html>
```